Silver Tsunami E-Blast to Customers

We are looking for a fresh e-blast design that is in line with company branding (prvreit.com). Please use the attached logo and include the copy below. The images below are inspiration. We’d like the image of a senior (older) woman surfer on a GINORMOUS wave crouched low.
Specs:
600px w x 1500px h
Copy:
(big, bold header) Ride the Wave with PRV's Financing Solutions!
The Silver Tsunami is surging ashore! Smart operators aren't bracing for impact, they're grabbing their boards and riding the wave of opportunity.
PRV has a full quiver of flexible financing solutions to help you stay afloat, whether you're looking to acquire, build, or refinance.
Get on board with PRV!
Attending GSH in San Diego?
Let's connect.
Our financing solutions include:
Acquisitions
Construction
Refinancing
Recapitalizations
Structured Leases
Bridge
Mezzanine
Unitranche
NNN Lease
Preferred Equity

```html
<!DOCTYPE html>
<html lang="en">
<head>
<meta charset="utf-8">
<title>Ride the Wave with PRV's Financing Solutions!</title>
<link rel="stylesheet" href="https://fonts.googleapis.com/css2?family=Poppins:wght@400;600;700;800&display=swap">
<style>
  :root {
    --backdrop: #f1f1f1;
    --card: #ffffff;
    --panel: #e3e3e3;
    --navy: #0b3192;
    --ink: #1b1b1b;
    --photo-light: #d9d9d9;
    --photo-mid: #8a8a8a;
    --photo-dark: #232323;
  }
  * { box-sizing: border-box; margin: 0; padding: 0; }
  html, body {
    width: 1200px; height: 1200px; overflow: hidden;
    background: var(--backdrop);
    font-family: "Poppins", sans-serif;
  }
  .eblast {
    position: absolute;
    left: 368px; top: 20px;
    width: 464px; height: 1160px;
    background: var(--card);
  }
  .hero-panel {
    position: absolute;
    left: 27px; top: 19px;
    width: 411px; height: 1025px;
    background: var(--panel);
    overflow: hidden;
  }
  .hero-photo {
    position: absolute;
    left: 0; bottom: 0;
    width: 100%; height: 400px;
    background: linear-gradient(180deg,
      var(--panel) 0%,
      var(--photo-light) 20%,
      var(--photo-mid) 52%,
      var(--photo-dark) 82%,
      #151515 100%);
  }
  .hero-copy {
    position: relative;
    padding: 84px 30px 0 40px;
    color: var(--ink);
  }
  .headline {
    font-weight: 800;
    font-size: 38px;
    line-height: 44px;
    color: var(--navy);
    letter-spacing: -0.2px;
    margin-bottom: 18px;
  }
  .intro {
    font-size: 13px;
    line-height: 21px;
    margin-bottom: 8px;
  }
  .tagline {
    font-size: 13px;
    line-height: 21px;
    font-weight: 700;
    color: var(--navy);
    margin-bottom: 8px;
  }
  .list-label {
    font-size: 13px;
    line-height: 21px;
    margin-bottom: 10px;
  }
  .solutions {
    list-style: none;
    display: grid;
    grid-template-columns: 165px 150px;
    grid-auto-flow: column;
    grid-template-rows: repeat(5, 21.6px);
    margin-left: 2px;
    margin-bottom: 12px;
  }
  .solutions li {
    font-size: 12.8px;
    line-height: 18px;
    display: flex;
    align-items: flex-end;
  }
  .solutions li span {
    border-bottom: 1px solid var(--navy);
    padding: 0 3px 0 6px;
  }
  .solutions li::before {
    content: "";
    width: 9px; height: 13px;
    background: var(--navy);
    flex: none;
  }
  .cta {
    font-size: 11.6px;
    line-height: 20px;
    font-weight: 700;
  }
  .footer {
    position: absolute;
    left: 33px; right: 14px; bottom: 0;
    height: 116px;
    display: flex;
    align-items: center;
    justify-content: space-between;
  }
  .footer .cta {
    font-size: 12.2px;
    line-height: 22px;
    color: #2a2a2a;
    width: 300px;
  }
  .brand {
    display: flex;
    align-items: center;
    gap: 8px;
    margin-right: 12px;
  }
  .brand-square {
    width: 20px; height: 20px;
    background: var(--navy);
  }
  .brand-name {
    font-weight: 800;
    font-size: 26px;
    color: var(--navy);
  }
</style>
</head>
<body>
  <main class="eblast">
    <section class="hero-panel">
      <div class="hero-photo" role="img" aria-label="Black and white photo of a senior woman surfer crouched low on her board riding a huge breaking wave"></div>
      <div class="hero-copy">
        <h1 class="headline">Ride the Wave<br>with PRV’s<br>Financing<br>Solutions!</h1>
        <p class="intro">The Silver Tsunami is surging ashore! Smart operators aren’t bracing for impact, they’re grabbing their boards and riding the wave of opportunity.</p>
        <p class="intro">PRV has a full quiver of flexible financing solutions to help you stay afloat, whether you’re looking to acquire, build, or refinance.</p>
        <p class="tagline">Get on board with PRV!</p>
        <p class="list-label">Our financing solutions include:</p>
        <ul class="solutions">
          <li><span>Acquisitions</span></li>
          <li><span>Construction</span></li>
          <li><span>Refinancing</span></li>
          <li><span>Recapitalizations</span></li>
          <li><span>Structured Leases</span></li>
          <li><span>Bridge</span></li>
          <li><span>Mezzanine</span></li>
          <li><span>Unitranche</span></li>
          <li><span>NNN Lease</span></li>
          <li><span>Preferred Equity</span></li>
        </ul>
        <p class="cta">Attending GSH in San Diego?<br>Let’s connect.</p>
      </div>
    </section>
    <footer class="footer">
      <p class="cta">Attending GSH in San Diego?<br>Let’s connect.</p>
      <div class="brand">
        <span class="brand-square"></span>
        <span class="brand-name">PRV</span>
      </div>
    </footer>
  </main>
</body>
</html>
```